Business Card for TVK, logo files already created

Please, can you assist with creating a Business card the TVK graphics which are already listed on www.brinmoretech.example
The business card should be modern and upmarket, textured designs are welcome. Please feel free to express yourself and be very bold with your design.

Target Market(s)

Cyber Security

Industry/Entity Type

Information Technology

Contact Information for Business Card

Company Name
Name
Title
Mobile
Fax or Tel
email
url

Font styles to use
Serif
Sans Serif

Colors
3277b5
85acd3
ffffff

```html
<!DOCTYPE html>
<html lang="en">
<head>
<meta charset="utf-8">
<title>TVK Business Card</title>
<link href="https://fonts.googleapis.com/css2?family=Open+Sans:wght@400;600;700&display=swap" rel="stylesheet">
<style>
  :root {
    --backdrop: #2b2b2e;
    --navy-deep: #121a4a;
    --navy: #17235a;
    --teal: #2f7f98;
    --ice: #c9dff2;
    --sky: #85acd3;
    --white: #ffffff;
    --arc: rgba(120, 190, 220, 0.45);
  }
  * { margin: 0; padding: 0; box-sizing: border-box; }
  html, body { width: 1200px; height: 900px; overflow: hidden; }
  body {
    background: var(--backdrop);
    font-family: "Open Sans", Arial, sans-serif;
    color: var(--white);
    position: relative;
  }
  .card {
    position: absolute;
    width: 560px;
    height: 320px;
    overflow: hidden;
    background: linear-gradient(180deg, var(--navy-deep) 0%, var(--navy) 62%, var(--teal) 100%);
    box-shadow: 0 14px 30px rgba(0,0,0,0.5);
  }
  .card-front { left: 80px; top: 100px; }
  .card-back { left: 560px; top: 480px; }
  .card-arcs { position: absolute; inset: 0; width: 100%; height: 100%; }

  .front-brand {
    position: absolute;
    left: 0; right: 0; top: 78px;
    text-align: center;
  }
  .front-mark {
    font-size: 84px;
    font-weight: 700;
    letter-spacing: 4px;
    line-height: 1;
    color: var(--ice);
  }
  .front-name {
    margin-top: 6px;
    font-size: 24px;
    font-weight: 700;
    letter-spacing: 3px;
    color: var(--ice);
  }
  .front-rule {
    width: 250px;
    height: 1px;
    background: var(--white);
    margin: 8px auto 6px;
    opacity: 0.8;
  }
  .front-tagline {
    font-size: 12px;
    letter-spacing: 2.5px;
    color: var(--white);
  }

  .back-brand {
    position: absolute;
    left: 70px; top: 140px;
    display: flex;
    align-items: center;
    gap: 10px;
  }
  .back-mark {
    font-size: 36px;
    font-weight: 700;
    letter-spacing: 2px;
    color: var(--ice);
  }
  .back-divider { width: 1px; height: 34px; background: var(--white); opacity: 0.7; }
  .back-name {
    font-size: 12px;
    font-weight: 700;
    letter-spacing: 1px;
    line-height: 1.2;
    color: var(--ice);
  }
  .contact-divider {
    position: absolute;
    left: 300px; top: 40px;
    width: 1px; height: 150px;
    background: linear-gradient(180deg, transparent, rgba(255,255,255,0.35), transparent);
  }
  .contact {
    position: absolute;
    left: 320px; top: 48px;
  }
  .person { font-size: 17px; letter-spacing: 1px; }
  .person strong { font-weight: 700; }
  .person span { font-weight: 400; }
  .role { font-size: 9px; letter-spacing: 1px; margin-bottom: 10px; color: var(--ice); }
  .contact-list { list-style: none; }
  .contact-list li {
    display: flex; align-items: center; gap: 8px;
    font-size: 11px; line-height: 20px;
  }
  .contact-list svg { width: 11px; height: 11px; fill: var(--white); flex: none; }
</style>
</head>
<body>

<section class="card card-front">
  <svg class="card-arcs" viewBox="0 0 560 320" aria-hidden="true">
    <circle cx="500" cy="120" r="75" fill="none" stroke="var(--arc)" stroke-width="1"/>
    <circle cx="-40" cy="210" r="80" fill="none" stroke="var(--arc)" stroke-width="1"/>
  </svg>
  <div class="front-brand">
    <div class="front-mark">TVK</div>
    <div class="front-name">BRINMORE TECH</div>
    <div class="front-rule"></div>
    <div class="front-tagline">INSIGHT - LED CYBER DEFENCE</div>
  </div>
</section>

<section class="card card-back">
  <svg class="card-arcs" viewBox="0 0 560 320" aria-hidden="true">
    <circle cx="520" cy="100" r="85" fill="none" stroke="var(--arc)" stroke-width="1"/>
    <circle cx="-30" cy="190" r="70" fill="none" stroke="var(--arc)" stroke-width="1"/>
  </svg>
  <div class="back-brand">
    <div class="back-mark">TVK</div>
    <div class="back-divider"></div>
    <div class="back-name">BRINMORE<br>TECH</div>
  </div>
  <div class="contact-divider"></div>
  <div class="contact">
    <div class="person"><strong>DANIEL</strong> <span>HART</span></div>
    <div class="role">FOUNDER AND CEO</div>
    <ul class="contact-list">
      <li><svg viewBox="0 0 12 12"><path d="M3 0h6a1 1 0 0 1 1 1v10a1 1 0 0 1-1 1H3a1 1 0 0 1-1-1V1a1 1 0 0 1 1-1zm0 1.5v8h6v-8z"/></svg>123-456-7890</li>
      <li><svg viewBox="0 0 12 12"><path d="M1 4c0-2 2-3 5-3s5 1 5 3l-2 1-1-1V3H4v1L3 5zM2 6h8l1 5H1z"/></svg>123-456-7890</li>
      <li><svg viewBox="0 0 12 12"><path d="M0 2h12v8H0zm1 1v.5l5 3.5 5-3.5V3z"/></svg>contact@brinmoretech.example</li>
      <li><svg viewBox="0 0 12 12"><path d="M6 0a6 6 0 1 0 0 12A6 6 0 0 0 6 0zm0 1.2c.8 0 1.6 2 1.7 4.2H4.3C4.4 3.2 5.2 1.2 6 1.2zM1.3 6.6h1.9c.1 1.6.4 3 .9 3.8a4.8 4.8 0 0 1-2.8-3.8zm3 0h3.4c-.1 2.2-.9 4.2-1.700 4.2s-1.6-2-1.7-4.2zm4.5 0h1.9a4.8 4.8 0 0 1-2.8 3.8c.5-.8.8-2.2.9-3.8zM1.3 5.4a4.8 4.8 0 0 1 2.8-3.8c-.5.8-.8 2.2-.9 3.8zm7.5 0c-.1-1.6-.4-3-.9-3.8a4.8 4.8 0 0 1 2.8 3.8z"/></svg>www.brinmoretech.example</li>
    </ul>
  </div>
</section>

</body>
</html>
```